Handover Document for post installation solar customers

I require a handover document (small A4 book) design for when we complete solar installations for our customers. It will need to have a brief description of next steps off the application process after installation aswell as some maintenance scheduling etc. This information will be provided by us.

Target Market(s)

Post installation customers (Solar)

Industry/Entity Type

Solar/ renewable

Colors
0054AA
0677BA
7BADD7
CADEEF
E8F1F8

Requirements
Must have
• Handover document provided in attatchment (must be made generic and not include customers details etc.) the attachment is only for reference. An intro "Thanks for using ZOV electrics.........". What happens next section
Nice to have
• Please use some of our past customers logos in our website - www.zovelectrics.com.au
Should not have
• Must be simple and look professional

```html
<!DOCTYPE html>
<html lang="en">
<head>
<meta charset="utf-8">
<title>Contents Page – Solar Handover Document</title>
<link href="https://fonts.googleapis.com/css2?family=Oswald:wght@600&family=Roboto+Condensed:wght@400;700&display=swap" rel="stylesheet">
<style>
  :root {
    --blue-deep: #0054AA;
    --blue-mid: #0677BA;
    --blue-soft: #7BADD7;
    --blue-pale: #CADEEF;
    --blue-mist: #E8F1F8;
    --text-grey: #3f4a57;
    --white: #ffffff;
  }
  html, body { margin: 0; padding: 0; overflow: hidden; }
  body { width: 849px; height: 1200px; background: var(--white); }
  .page {
    position: relative;
    width: 849px; height: 1200px; overflow: hidden;
    background:
      radial-gradient(ellipse 620px 520px at 0% 100%, var(--blue-pale) 0%, var(--blue-mist) 45%, rgba(255,255,255,0) 80%),
      var(--white);
    font-family: "Roboto Condensed", "Arial Narrow", sans-serif;
  }
  .title-tab {
    position: absolute; left: 0; top: 48px;
    width: 395px; height: 94px;
    background: var(--blue-deep);
    border-radius: 0 26px 26px 0;
    display: flex; align-items: center; padding-left: 22px; box-sizing: border-box;
  }
  .title-tab h1 {
    margin: 0; color: var(--white);
    font-family: "Oswald", "Arial Narrow", sans-serif;
    font-weight: 600; font-size: 54px; letter-spacing: 0.5px; line-height: 1;
    white-space: nowrap;
  }
  .decor { position: absolute; left: 0; top: 0; }
  .contents { position: absolute; left: 38px; top: 192px; width: 540px; }
  .section { margin: 0; }
  .section h2 {
    margin: 0; color: var(--blue-deep);
    font-weight: 700; font-size: 31px; line-height: 38px;
    white-space: nowrap;
  }
  .section ol {
    list-style: none; margin: 0 0 2px 2px; padding: 0;
  }
  .section li {
    color: var(--text-grey); font-size: 12.5px; line-height: 17.5px;
    white-space: nowrap;
  }
</style>
</head>
<body>
<main class="page">

  <svg class="decor" width="849" height="1200" viewBox="0 0 849 1200">
    <defs>
      <linearGradient id="roofSky" x1="0" y1="0" x2="1" y2="1">
        <stop offset="0" stop-color="#9cc6ea"/>
        <stop offset="1" stop-color="#1f4f86"/>
      </linearGradient>
      <linearGradient id="panelField" x1="0" y1="0" x2="1" y2="1">
        <stop offset="0" stop-color="#c9dcee"/>
        <stop offset="1" stop-color="#22497a"/>
      </linearGradient>
      <linearGradient id="productBg" x1="0" y1="0" x2="0" y2="1">
        <stop offset="0" stop-color="#ffffff"/>
        <stop offset="1" stop-color="#dbe8f4"/>
      </linearGradient>
    </defs>

    <circle cx="708" cy="85" r="160" fill="none" stroke="var(--blue-pale)" stroke-width="10"/>
    <circle cx="736" cy="552" r="192" fill="none" stroke="var(--blue-mist)" stroke-width="14"/>
    <path d="M560 420 A190 190 0 0 1 849 330" fill="none" stroke="var(--blue-mid)" stroke-width="6"/>
    <path d="M580 760 A190 190 0 0 0 849 780" fill="none" stroke="var(--blue-soft)" stroke-width="6"/>

    <circle cx="708" cy="85" r="146" fill="var(--blue-mid)"/>
    <circle cx="708" cy="85" r="140" fill="url(#roofSky)" role="img" aria-label="Photo of an installer fitting solar panels on a roof"/>

    <circle cx="736" cy="552" r="176" fill="var(--blue-deep)"/>
    <circle cx="736" cy="552" r="170" fill="url(#panelField)" role="img" aria-label="Photo of solar panels installed on a house roof under a blue sky"/>

    <circle cx="623" cy="311" r="120" fill="var(--blue-deep)"/>
    <circle cx="623" cy="311" r="112" fill="url(#productBg)" role="img" aria-label="Product image of a solar panel on a tilted mounting frame"/>
  </svg>

  <header class="title-tab"><h1>CONTENTS PAGE</h1></header>

  <nav class="contents">
    <section class="section"><h2>1 Introduction</h2></section>
    <section class="section"><h2>2 Contact Information</h2>
      <ol><li>2.1 Installation Company</li><li>2.2 Accredited Installer</li></ol></section>
    <section class="section"><h2>3 Precautions and warnings</h2>
      <ol><li>3.1 Warning symbols</li><li>3.2 Important Safety Information</li></ol></section>
    <section class="section"><h2>4 Emergency Procedures</h2>
      <ol><li>4.1 Earth Fault Alarm</li><li>4.2 Shutdown Procedure</li></ol></section>
    <section class="section"><h2>5 System Description</h2>
      <ol><li>5.1 PV System Summary</li><li>5.2 Components</li><li>5.3 System Congiuration</li><li>5.4 Component Locations</li></ol></section>
    <section class="section"><h2>6 System Performance</h2>
      <ol><li>6.1 Production Estimates</li><li>6.2 Estimated Savings</li></ol></section>
    <section class="section"><h2>7 Connection Diagram</h2></section>
    <section class="section"><h2>8 Equipment Supplied</h2>
      <ol><li>8.1 Bill of Materials</li></ol></section>
    <section class="section"><h2>9 Maintenance Information</h2>
      <ol><li>9.1 Recommended Maintenance Schedule</li><li>9.2 Information for Maintenance Sta</li><li>9.3 Maintenance Logs</li></ol></section>
    <section class="section"><h2>10 Commissioning Report</h2>
      <ol><li>10.1 Installation Checklist</li><li>10.2 Test Records</li><li>10.3 Declaration of Compliance</li></ol></section>
    <section class="section"><h2>11 Warranty InformationAppendix</h2>
      <ol><li>A: Equipment DocumentationAppendix</li><li>B: Warranty DocumentationAppendix</li><li>C: DisclaimersAppendix</li><li>D: CommissioningContents Page</li></ol></section>
  </nav>

</main>
</body>
</html>
```